Travel Company is looking for a STAND OUT Business Card

I need a unique Business Card that will truly stand out. Nothing too busy. Simple is good, right? Not looking for a standard design either. No cookie cutter layout. We are a Travel Company that works more with Companies than Travelers. I had an idea to focus and emphasis on the 2 logo a bit more. This is not necessary, however thought it would look interesting. I am just looking for something interesting and a bit different. Does't have to completely off the wall crazy, just not your run of the mill business card.

Target Market(s)

Hoteliers, Resort Management, Call Centers, Executives, Travelers, Families, Businesses

Industry/Entity Type

Hospitality

Contact Information for Business Card

President/CEO - Marcus T Bellamy (title not necessary if design doesn't allow for it)
contact - (407) 555-0186
email - mbellamy@wayfarenow.example
address - 4812 Quillmore Ave #164
Orlando, FL 32804
website - www.wayfarenow.example

Font styles to use
Serif
Other font styles liked:
• Avenir Next LT Pro BOLD

Requirements
Must have
• simple look and design. Unique design
Nice to have
• I attached the 2 logo separate from the main logo. This can be used separately from the Main Logo, together with the main logo or as main logo. I included the logo font. Use it or not, designers choice.
Should not have
• cookie cutter design. Little use of red other than the logo

```html
<!DOCTYPE html>
<html lang="en">
<head>
<meta charset="utf-8">
<title>Wayfare Now — Business Card</title>
<link rel="stylesheet" href="https://fonts.googleapis.com/css2?family=Montserrat:wght@400;500;700;800&display=swap">
<style>
  :root {
    --backdrop: #e6e3dd;
    --paper: #ffffff;
    --brand-red: #f2393b;
    --brand-red-deep: #c81e22;
    --charcoal: #3a4240;
    --ink: #1f1f1f;
    --watermark: #f65a5c;
  }
  * { box-sizing: border-box; margin: 0; padding: 0; }
  html, body {
    width: 1200px; height: 1124px; overflow: hidden;
    background: var(--backdrop);
    font-family: "Montserrat", "Helvetica Neue", Arial, sans-serif;
  }
  .sheet {
    position: relative; width: 1200px; height: 1124px;
  }
  .card {
    position: absolute; left: 180px; width: 840px; height: 480px;
    background: var(--paper); border-radius: 36px; overflow: hidden;
    box-shadow: 0 18px 40px rgba(0,0,0,.12), 0 3px 8px rgba(0,0,0,.08);
  }
  .card--back { top: 52px; }
  .card--front { top: 592px; }

  /* back */
  .wordmark {
    position: absolute; top: 170px; left: 0; width: 100%;
    display: flex; align-items: center; justify-content: center; gap: 16px;
    font-weight: 800; font-size: 64px; color: var(--ink); letter-spacing: -1px;
  }
  .wordmark__dot {
    width: 30px; height: 30px; border-radius: 50%; background: var(--brand-red);
  }
  .back-trim { position: absolute; left: 0; bottom: 0; width: 100%; height: 110px; }
  .back-url {
    position: absolute; bottom: 26px; left: 340px; width: 280px; text-align: center;
    color: #fff; font-size: 17px; letter-spacing: .5px;
  }

  /* front */
  .front-band { position: absolute; inset: 0; width: 100%; height: 100%; }
  .watermark {
    position: absolute; top: 118px; left: 46px;
    font-weight: 800; font-size: 70px; color: var(--watermark); letter-spacing: -1px;
  }
  .identity {
    position: absolute; top: 30px; right: 44px; text-align: right; color: #fff;
  }
  .identity__name { font-weight: 800; font-size: 30px; letter-spacing: .5px; }
  .identity__title { font-weight: 400; font-size: 19px; letter-spacing: .8px; margin-top: 2px; }
  .brand-disc {
    position: absolute; top: 120px; right: 54px; width: 96px; height: 96px;
    border-radius: 50%; background: var(--paper); border: 8px solid var(--brand-red);
  }
  .contacts {
    position: absolute; top: 270px; left: 40px; right: 40px;
    display: grid; grid-template-columns: 1fr 1fr; column-gap: 40px; row-gap: 22px;
  }
  .contact {
    display: flex; align-items: center; justify-content: flex-end; gap: 14px;
    font-size: 19px; color: var(--ink); letter-spacing: .3px; text-align: right; line-height: 1.25;
  }
  .contact__icon {
    flex: none; width: 38px; height: 38px; border-radius: 50%;
    background: var(--brand-red-deep); display: grid; place-items: center;
    box-shadow: 0 0 0 4px #eee;
  }
  .contact__icon svg { width: 20px; height: 20px; }
  .front-trim { position: absolute; left: 0; bottom: 0; width: 100%; height: 30px; }
</style>
</head>
<body>
<main class="sheet">

  <section class="card card--back" aria-label="Card back">
    <div class="wordmark"><span class="wordmark__dot"></span>wayfarenow</div>
    <svg class="back-trim" viewBox="0 0 840 110" preserveAspectRatio="none">
      <polygon points="0,86 840,30 840,58 0,110" fill="var(--brand-red)"/>
      <polygon points="330,110 330,56 600,38 630,110" fill="var(--charcoal)"/>
    </svg>
    <div class="back-url">www.wayfarenow.example</div>
  </section>

  <section class="card card--front" aria-label="Card front">
    <svg class="front-band" viewBox="0 0 840 480" preserveAspectRatio="none">
      <polygon points="0,0 840,0 840,100 690,100 690,215 0,215" fill="var(--brand-red)"/>
      <polygon points="560,480 560,464 840,456 840,480" fill="var(--brand-red)"/>
      <polygon points="0,480 0,470 560,464 560,480" fill="var(--charcoal)"/>
    </svg>
    <div class="watermark">wayfarenow</div>
    <div class="identity">
      <div class="identity__name">Marcus T Bellamy</div>
      <div class="identity__title">President / CEO</div>
    </div>
    <div class="brand-disc"></div>

    <div class="contacts">
      <div class="contact">(407) 555-0186
        <span class="contact__icon"><svg viewBox="0 0 24 24"><path fill="#fff" d="M6.6 10.8a15 15 0 0 0 6.6 6.6l2.2-2.2a1 1 0 0 1 1-.25 11.4 11.4 0 0 0 3.6.57 1 1 0 0 1 1 1V20a1 1 0 0 1-1 1A17 17 0 0 1 3 4a1 1 0 0 1 1-1h3.5a1 1 0 0 1 1 1c0 1.25.2 2.45.57 3.57a1 1 0 0 1-.25 1z"/></svg></span>
      </div>
      <div class="contact">mbellamy@wayfarenow.example
        <span class="contact__icon"><svg viewBox="0 0 24 24"><rect x="3" y="6" width="18" height="12" rx="1.5" fill="#fff"/><path d="M3.5 6.8 12 13l8.5-6.2" stroke="var(--brand-red-deep)" stroke-width="1.6" fill="none"/></svg></span>
      </div>
      <div class="contact">www.wayfarenow.example
        <span class="contact__icon"><svg viewBox="0 0 24 24" fill="none" stroke="#fff" stroke-width="1.8"><circle cx="12" cy="12" r="8.5"/><ellipse cx="12" cy="12" rx="3.8" ry="8.5"/><path d="M3.5 12h17"/></svg></span>
      </div>
      <div class="contact">4812 Quillmore Ave #164<br>Orlando, FL 32804
        <span class="contact__icon"><svg viewBox="0 0 24 24"><path fill="#fff" d="M12 2a7 7 0 0 0-7 7c0 5 7 13 7 13s7-8 7-13a7 7 0 0 0-7-7zm0 9.5A2.5 2.5 0 1 1 12 6.5a2.5 2.5 0 0 1 0 5z"/></svg></span>
      </div>
    </div>
    <svg class="front-trim" viewBox="0 0 840 30" preserveAspectRatio="none"></svg>
  </section>

</main>
</body>
</html>
```